当寺院に「ほたる舞観音」という「ほたる舞」の徳がある観音さまをおまつりしております。その「ほたる舞観音」のお守りを作成することになりましたので、そのお守りのカバーデザインをお願いします。どうぞ、お力をお貸し頂ければと思います。

当寺院の「ほたる舞観音」さまです。
わかりにくい画像ですが、参考にしてください。
https://hoshinagi-in.jp/keidaigoannai.html
■さざなみ観音・ほたる舞観音 の場所になります。

「ほたる舞」という徳からも、主にご年配の方向けのお守りになります。代わりに若年層の方も求められる方もいると思います。デザインはお任せします。希望の色も参考までにして頂いて、基本は自由で構いません。

こちらのお守り制作会社にお願いして製造して頂く予定です。
https://tsurugaya-shouten.co.jp/wordpress_5/jyuyohin
https://tsurugaya-shouten.co.jp/omamori3.pdf
お守りの大きさは、標準サイズW45mm×H75mmです。
上記サイトのお守り用AIテンプレートを使用して頂いての入稿という形でお願いします。

「ほたる舞観音」さまと対になる「さざなみ観音」さまもおまつりしており、今回の「ほたる舞観音」の反響が良ければ「さざなみ観音」のお守りの作成も考えております。
1点
黄・オレンジ系、紫系、無彩色系、参考までに希望しただけですので、基本はお任せします。
ほたる舞観音さまは、十一面観音さまになります。
どうぞご参考までにお願いします。

デザインがとても良く選ばさせていただきました。

丁寧に作成していただいてありがとうございます。

```html
<!DOCTYPE html>
<html lang="ja">
<head>
<meta charset="utf-8">
<title>ほたる舞観音 お守り W45×H75（mm）用 テンプレート</title>
<link rel="stylesheet" href="https://fonts.googleapis.com/css2?family=Zen+Maru+Gothic:wght@500;700;900&family=Noto+Sans+JP:wght@400;700&display=swap">
<style>
  :root {
    --paper: #ffffff;
    --ink: #222222;
    --label-teal: #2aa3c7;
    --amulet-orange: #f2a731;
    --amulet-edge: #9fd3df;
    --title-red: #d2452c;
    --plate-white: #ffffff;
    --portrait-cream: #f6d9b6;
    --portrait-grey: #b9b3ab;
  }
  html, body {
    margin: 0;
    padding: 0;
    overflow: hidden;
    background: var(--paper);
  }
  .sheet {
    position: relative;
    width: 849px;
    height: 1200px;
    overflow: hidden;
    background: var(--paper);
    font-family: "Zen Maru Gothic", sans-serif;
  }
  .sheet-caption {
    position: absolute;
    left: 18px;
    top: 22px;
    margin: 0;
    font-family: "Noto Sans JP", sans-serif;
    font-weight: 400;
    font-size: 14px;
    color: var(--ink);
    letter-spacing: 0.02em;
  }
  .side-label {
    position: absolute;
    top: 100px;
    margin: 0;
    font-family: "Noto Sans JP", sans-serif;
    font-weight: 700;
    font-size: 34px;
    color: var(--label-teal);
    transform: translateX(-50%);
    letter-spacing: 0.04em;
  }
  .side-label--front { left: 283px; }
  .side-label--back { left: 590px; }

  .amulet {
    position: absolute;
    overflow: hidden;
  }
  .amulet-shape {
    position: absolute;
    inset: 0;
    width: 100%;
    height: 100%;
  }
  .amulet--small { width: 255px; height: 396px; top: 170px; font-size: 25.5px; }
  .amulet--large { width: 340px; height: 538px; top: 651px; font-size: 34px; }
  .amulet--small.amulet--front { left: 156px; }
  .amulet--small.amulet--back { left: 465px; }
  .amulet--large.amulet--front { left: 99px; }
  .amulet--large.amulet--back { left: 467px; }

  .vertical {
    position: absolute;
    margin: 0;
    writing-mode: vertical-rl;
    text-orientation: upright;
    line-height: 1;
  }
  .blessing-plate {
    left: 54%;
    top: 9%;
    height: 28%;
    width: 1.25em;
    background: var(--plate-white);
    color: var(--title-red);
    font-weight: 700;
    font-size: 0.85em;
    display: flex;
    align-items: center;
    justify-content: center;
    box-sizing: border-box;
    letter-spacing: 0.08em;
  }
  .amulet-title {
    left: 20%;
    top: 18%;
    color: var(--title-red);
    font-weight: 900;
    font-size: 3.2em;
    letter-spacing: 0.02em;
  }
  .couple-portrait {
    position: absolute;
    left: 8%;
    top: 60%;
    width: 84%;
    height: 37%;
    border-radius: 45% 45% 8% 8% / 55% 55% 8% 8%;
    background: linear-gradient(90deg, var(--portrait-cream) 0%, var(--portrait-cream) 50%, var(--portrait-grey) 50%, var(--portrait-grey) 100%);
  }
  .deity-name {
    left: 50%;
    top: 16%;
    transform: translateX(-50%);
    color: var(--plate-white);
    font-weight: 700;
    font-size: 1.42em;
    letter-spacing: 0;
  }

  .enlarge-arrow {
    position: absolute;
    top: 578px;
    width: 40px;
    height: 62px;
  }
  .enlarge-arrow--front { left: 263px; }
  .enlarge-arrow--back { left: 546px; }
  .enlarge-label {
    position: absolute;
    left: 425px;
    top: 588px;
    margin: 0;
    transform: translateX(-50%);
    font-family: "Noto Sans JP", sans-serif;
    font-weight: 400;
    font-size: 30px;
    color: var(--ink);
  }
</style>
</head>
<body>
<main class="sheet">
  <p class="sheet-caption">お守り　W45×H75（mm）用　テンプレート</p>

  <h2 class="side-label side-label--front">表面</h2>
  <h2 class="side-label side-label--back">裏面</h2>

  <!-- Front, actual size -->
  <section class="amulet amulet--small amulet--front" aria-label="表面">
    <svg class="amulet-shape" viewBox="0 0 90 140" preserveAspectRatio="none" aria-hidden="true">
      <polygon points="1,26 25,1 65,1 89,26 89,139 1,139" fill="var(--amulet-orange)" stroke="var(--amulet-edge)" stroke-width="1.2"/>
    </svg>
    <p class="vertical blessing-plate">ほたる舞</p>
    <p class="vertical amulet-title">御守</p>
    <div class="couple-portrait" role="img" aria-label="笑顔の年配の夫婦のイラスト"></div>
  </section>

  <!-- Back, actual size -->
  <section class="amulet amulet--small amulet--back" aria-label="裏面">
    <svg class="amulet-shape" viewBox="0 0 90 140" preserveAspectRatio="none" aria-hidden="true">
      <polygon points="1,26 25,1 65,1 89,26 89,139 1,139" fill="var(--amulet-orange)" stroke="var(--amulet-edge)" stroke-width="1.2"/>
    </svg>
    <p class="vertical deity-name">ほたる舞観音</p>
  </section>

  <svg class="enlarge-arrow enlarge-arrow--front" viewBox="0 0 40 62" aria-hidden="true">
    <polygon points="12,0 28,0 28,34 40,34 20,62 0,34 12,34" fill="var(--ink)"/>
  </svg>
  <p class="enlarge-label">拡大</p>
  <svg class="enlarge-arrow enlarge-arrow--back" viewBox="0 0 40 62" aria-hidden="true">
    <polygon points="12,0 28,0 28,34 40,34 20,62 0,34 12,34" fill="var(--ink)"/>
  </svg>

  <!-- Front, enlarged -->
  <section class="amulet amulet--large amulet--front" aria-label="表面（拡大）">
    <svg class="amulet-shape" viewBox="0 0 90 140" preserveAspectRatio="none" aria-hidden="true">
      <polygon points="1,26 25,1 65,1 89,26 89,139 1,139" fill="var(--amulet-orange)" stroke="var(--amulet-edge)" stroke-width="1"/>
    </svg>
    <p class="vertical blessing-plate">ほたる舞</p>
    <p class="vertical amulet-title">御守</p>
    <div class="couple-portrait" role="img" aria-label="笑顔の年配の夫婦のイラスト"></div>
  </section>

  <!-- Back, enlarged -->
  <section class="amulet amulet--large amulet--back" aria-label="裏面（拡大）">
    <svg class="amulet-shape" viewBox="0 0 90 140" preserveAspectRatio="none" aria-hidden="true">
      <polygon points="1,26 25,1 65,1 89,26 89,139 1,139" fill="var(--amulet-orange)" stroke="var(--amulet-edge)" stroke-width="1"/>
    </svg>
    <p class="vertical deity-name">ほたる舞観音</p>
  </section>
</main>
</body>
</html>
```